Financial Workshop for Hollister Wealth

Postcard to comply with RMPS. Invitation to workshop for 55+ senior community.
"Estate Conservation Strategies and Legacy Planning"
Building a sound and lasting retirement portfolio with a focus on growth and asset protection.
Developing investment objectives
Understanding risk adversity
Preserving assets
Conservative growth strategies for saving and investing
Planning for uncovered health care costs
Estate planning
Dale Whitford, Chartered Money Counselorâ„¢

add to the text (bullets) after Estate Planning (on same line) and Wealth Transfer Strategies Thank you Added Friday, October 13, 2017

Target Market(s)

Seniors

Industry/Entity Type

Financial

Font styles to use
Sans Serif

Colors

Designer to choose colors to be used in the design.

Requirements
Must have
• Logo
• Eye-catching images
• Easy to read geared for seniors
• Upscale professional look
• Afresh new look from previous samples sent.
Nice to have
• Something that stands out among the many postcard mail pieces they will get.
Should not have
• aside from logo/photo samples are an example of previous workshops and should not be reused.

```html
<!DOCTYPE html>
<html lang="en">
<head>
<meta charset="utf-8">
<title>Hollister Wealth – Workshop Postcard</title>
<link href="https://fonts.googleapis.com/css2?family=Montserrat:wght@400;600;700&display=swap" rel="stylesheet">
<style>
  :root {
    --navy: #2e2d83;
    --navy-deep: #24236b;
    --sky: #7cc3f5;
    --tick: #3a8ee6;
    --ink: #222230;
    --white: #ffffff;
    --black: #0b0b0b;
    --stage: #eceef2;
    --rule: #d9dae0;
  }
  * { box-sizing: border-box; margin: 0; padding: 0; }
  html, body { width: 1200px; height: 1000px; overflow: hidden; }
  body {
    background: var(--stage);
    font-family: "Montserrat", Arial, sans-serif;
    color: var(--ink);
    position: relative;
  }
  .postcard {
    position: absolute;
    left: 50px; top: 160px;
    width: 1100px; height: 680px;
    background: var(--white);
    overflow: hidden;
    box-shadow: 0 10px 30px rgba(0,0,0,.18);
  }
  .postcard-shapes { position: absolute; inset: 0; }

  .brand {
    position: absolute;
    left: 60px; top: 100px;
    display: flex; align-items: center; gap: 16px;
  }
  .brand-mark {
    width: 34px; height: 34px;
    background: var(--navy);
  }
  .brand-name {
    font-weight: 600;
    font-size: 34px;
    letter-spacing: 3px;
    text-transform: uppercase;
    color: var(--navy);
  }

  .workshop {
    position: absolute;
    left: 40px; top: 288px;
    width: 640px;
  }
  .workshop-title {
    font-weight: 700;
    font-size: 23px;
    line-height: 26px;
    color: var(--navy);
    margin-bottom: 8px;
  }
  .topic-list { list-style: none; }
  .topic-list li {
    position: relative;
    padding-left: 30px;
    font-size: 19px;
    font-weight: 600;
    line-height: 26px;
    color: var(--ink);
  }
  .topic-list li::before {
    content: "";
    position: absolute;
    left: 0; top: 8px;
    width: 16px; height: 16px;
    border-radius: 50%;
    background: var(--tick);
  }
  .topic-list li::after {
    content: "";
    position: absolute;
    left: 5px; top: 10px;
    width: 4px; height: 8px;
    border: solid var(--white);
    border-width: 0 2px 2px 0;
    transform: rotate(45deg);
  }

  .advisor {
    position: absolute;
    left: 836px; top: 324px;
    color: var(--white);
  }
  .advisor-name { font-weight: 700; font-size: 25px; line-height: 30px; }
  .advisor-title { font-weight: 400; font-size: 16px; line-height: 20px; opacity: .9; }

  .contact {
    position: absolute;
    left: 712px; top: 436px;
    width: 370px;
    color: var(--white);
    font-size: 23px;
    line-height: 34px;
    font-weight: 600;
    white-space: nowrap;
  }
  .contact-accent { color: var(--sky); font-weight: 700; }
</style>
</head>
<body>
  <section class="postcard">
    <svg class="postcard-shapes" width="1100" height="680" viewBox="0 0 1100 680">
      <defs>
        <linearGradient id="photoTone" x1="0" y1="0" x2="1" y2="0">
          <stop offset="0" stop-color="#ffffff" stop-opacity="0"/>
          <stop offset="0.18" stop-color="#f3efd8"/>
          <stop offset="0.45" stop-color="#e9e3c6"/>
          <stop offset="0.7" stop-color="#c9dcef"/>
          <stop offset="1" stop-color="#f1f2f4"/>
        </linearGradient>
        <radialGradient id="portraitTone" cx="0.5" cy="0.4" r="0.6">
          <stop offset="0" stop-color="#d9b3a0"/>
          <stop offset="1" stop-color="#8a8d96"/>
        </radialGradient>
        <clipPath id="photoClip">
          <path d="M0,0 H1100 V170 C700,250 300,215 0,245 Z"/>
        </clipPath>
      </defs>

      <rect class="photo-area" x="400" y="0" width="700" height="260" fill="url(#photoTone)"
            clip-path="url(#photoClip)" role="img"
            aria-label="Photo of a senior couple reviewing financial papers together"/>

      <path class="navy-field" d="M0,245 C300,215 700,250 1100,170 V618 H0 Z" fill="var(--navy)"/>
      <path class="light-swoosh" d="M0,243 C300,213 700,248 1100,168" fill="none" stroke="#ffffff" stroke-width="5"/>
      <path class="content-field" d="M0,282 C250,250 520,258 620,298 C700,335 690,520 740,618 H0 Z" fill="var(--white)"/>
      <path class="content-edge" d="M0,282 C250,250 520,258 620,298" fill="none" stroke="var(--rule)" stroke-width="3"/>

      <circle cx="760" cy="335" r="68" fill="var(--white)"/>
      <circle cx="760" cy="335" r="62" fill="url(#portraitTone)" role="img" aria-label="Portrait of Dale Whitford"/>

      <rect class="footer-rule" x="0" y="612" width="1100" height="8" fill="var(--white)"/>
      <rect class="footer-band" x="0" y="620" width="1100" height="60" fill="var(--black)"/>
    </svg>

    <div class="brand">
      <span class="brand-mark"></span>
      <span class="brand-name">Hollister Wealth</span>
    </div>

    <div class="workshop">
      <h1 class="workshop-title">Estate Conservation Strategies<br>and Legacy Planning</h1>
      <ul class="topic-list">
        <li>Building a sound and lasting retirement portfolio<br>with a focus on growth and asset protection.</li>
        <li>Developing investment objectives</li>
        <li>Understanding risk adversity</li>
        <li>Preserving assets</li>
        <li>Conservative growth strategies for<br>saving and investing</li>
        <li>Planning for uncovered health care costs</li>
        <li>Estate planning and Wealth Transfer Strategies</li>
      </ul>
    </div>

    <div class="advisor">
      <p class="advisor-name">Dale Whitford</p>
      <p class="advisor-title">Chartered Money Counselor™</p>
    </div>

    <div class="contact">
      <p>For more information visit</p>
      <p class="contact-accent">www.hollisterwealth.com</p>
      <p>or call <span class="contact-accent">(555) 214-0387</span></p>
    </div>
  </section>
</body>
</html>
```